Business cards and logo for Delcourt Law, P.A.

I need a business card and logo design for a new law firm in Miami, Florida called Delcourt Law, P.A. I, Theodore K. Delcourt, am the only lawyer in the firm. The law firm will mainly serve businesses but will also handle many other cases. Preferred colors are green and/or gray, but open minded to other suggestions.

Industry/Entity Type

Legal

Contact Information for Business Card

Phone Number TBD. Address is:
41 NE 3RD AVE STE 200
MIAMI, FL 33142

```html
<!DOCTYPE html>
<html lang="en">
<head>
<meta charset="utf-8">
<title>Delcourt Law, P.A. — Business Card</title>
<link rel="stylesheet" href="https://fonts.googleapis.com/css2?family=Arimo:wght@400;700&display=swap">
<style>
  :root {
    --backdrop: #c9c9c9;
    --card-light-top: #ffffff;
    --card-light-bottom: #e4e4e4;
    --card-dark: #0b0b0b;
    --ink: #161616;
    --paper-text: #e6e6e6;
    --muted-text: #9a9a9a;
    --divider: #5a5a5a;
    --icon-fill: #d8d8d8;
  }
  * { margin: 0; padding: 0; box-sizing: border-box; }
  html, body { width: 1200px; height: 873px; overflow: hidden; }
  body {
    background: radial-gradient(ellipse at 50% 30%, #ededed 0%, var(--backdrop) 70%, #a9a9a9 100%);
    font-family: "Arimo", Arial, sans-serif;
  }
  .business-card {
    position: absolute;
    left: 180px; top: 196px;
    width: 840px; height: 480px;
    box-shadow: 0 18px 40px rgba(0,0,0,.35);
    overflow: hidden;
  }
  .card-brand-band {
    height: 260px;
    background: linear-gradient(180deg, var(--card-light-top), var(--card-light-bottom));
    display: flex; align-items: center; justify-content: center;
  }
  .firm-lockup { display: flex; align-items: center; gap: 22px; }
  .firm-mark { width: 40px; height: 40px; background: var(--ink); }
  .firm-name {
    font-weight: 700;
    font-size: 40px;
    letter-spacing: 1px;
    color: var(--ink);
    line-height: 1;
    text-transform: uppercase;
  }
  .card-contact-band {
    height: 220px;
    background: var(--card-dark);
    display: flex; align-items: center;
    position: relative;
  }
  .card-contact-band::before {
    content: ""; position: absolute;
    left: 420px; top: 30px; bottom: 30px; width: 1px;
    background: linear-gradient(180deg, transparent, var(--divider), transparent);
  }
  .person-block { width: 420px; padding-left: 80px; }
  .person-name {
    font-weight: 700; font-size: 20px; letter-spacing: .5px;
    color: var(--paper-text); text-transform: uppercase;
    white-space: nowrap;
  }
  .person-role {
    font-size: 16px; color: var(--muted-text);
    margin: 4px 0 22px 60px;
  }
  .person-email { font-size: 18px; color: var(--paper-text); }
  .contact-list {
    list-style: none; padding-left: 50px;
    display: flex; flex-direction: column; gap: 9px;
  }
  .contact-item {
    display: flex; align-items: flex-start; gap: 12px;
    font-size: 17px; line-height: 20px; color: var(--paper-text);
  }
  .contact-icon { width: 20px; height: 20px; flex: none; }
</style>
</head>
<body>
  <article class="business-card">
    <section class="card-brand-band">
      <div class="firm-lockup">
        <div class="firm-mark" aria-hidden="true"></div>
        <div class="firm-name">Delcourt Law, P.A.</div>
      </div>
    </section>
    <section class="card-contact-band">
      <div class="person-block">
        <div class="person-name">Theodore K. Delcourt</div>
        <div class="person-role">Lawyer</div>
        <div class="person-email">theodore@delcourtlaw.com</div>
      </div>
      <ul class="contact-list">
        <li class="contact-item">
          <svg class="contact-icon" viewBox="0 0 20 20" aria-label="Phone">
            <circle cx="10" cy="10" r="10" fill="var(--icon-fill)"/>
            <path d="M5 8 Q10 4 15 8 L13.5 9.5 L12 8.5 L8 8.5 L6.5 9.5 Z M7 10 H13 L14 14 H6 Z" fill="#0b0b0b"/>
          </svg>
          305 555-0142
        </li>
        <li class="contact-item">
          <svg class="contact-icon" viewBox="0 0 20 20" aria-label="Fax">
            <circle cx="10" cy="10" r="10" fill="var(--icon-fill)"/>
            <rect x="7" y="5" width="6" height="4" fill="#0b0b0b"/>
            <rect x="5" y="9" width="10" height="5" rx="1" fill="#0b0b0b"/>
          </svg>
          305 555-0187
        </li>
        <li class="contact-item">
          <svg class="contact-icon" viewBox="0 0 20 20" aria-label="Website">
            <circle cx="10" cy="10" r="10" fill="var(--icon-fill)"/>
            <rect x="5" y="6.5" width="10" height="7" fill="#0b0b0b"/>
            <path d="M5 6.5 L10 10.5 L15 6.5" stroke="#d8d8d8" stroke-width="1" fill="none"/>
          </svg>
          www.delcourtlaw.com
        </li>
        <li class="contact-item">
          <svg class="contact-icon" viewBox="0 0 20 20" aria-label="Address">
            <circle cx="10" cy="10" r="10" fill="var(--icon-fill)"/>
            <path d="M10 4 C7.5 4 6 5.8 6 8 C6 11 10 16 10 16 C10 16 14 11 14 8 C14 5.8 12.5 4 10 4 Z" fill="#0b0b0b"/>
            <circle cx="10" cy="8" r="1.6" fill="#d8d8d8"/>
          </svg>
          <span>41 NE 3RD AVE STE 200<br>MIAMI, FL 33142</span>
        </li>
      </ul>
    </section>
  </article>
</body>
</html>
```